Harvest Wing Guild Needs an Infographic

We are looking for an engaging infographic that will illustrate the steps and skill set needed to become an agricultural pilot. The infographic will be used in print and on the web. Print formats could include an 8.5" x 11" page or 17" x 11" spread/poster in a magazine and should also be scalable so that it can be printed as a larger poster. The web-ready infographic will be used on the association's website and Chirpbook page. Agricultural aviation is an exciting profession, but it is not always apparent or easy to get started in the industry. This infographic will focus on the requirements, training options, skills/mindset, working conditions, and income potential for someone interested in becoming an agricultural pilot, as well as the need for agricultural aviation services. The working title for the infographic is, "The Hunt for the Nation's Fresh Field Flyers Begins!" I am uploading a Word document with the proposed text. What we would like a graphic designer to do is turn that text into something highly visual/graphical. The supplied text can be pared down, if necessary, or used as a guide to accomplish the appropriate balance between the words, images, and graphics. The final design should be professional but appeal to people, primarily males, between the ages of 17-30.
Updates

We have increased the budget for our infographic design project!

Project Deadline Extended
Reason: We have extended our deadline to give designers interested in submitting an infographic design more time. We would appreciate any designs you can send our way!

Target Market(s)

This infographic is aimed at people between the ages of 17-30, predominantly males, interested flying and a possible career in agricultural aviation. A lot of people may be pilots who are interested in agricultural aviation, but they don't know how go about it. Typically, potential ag pilots have lived in a rural area and enjoy the outdoors. Due to the small size of the industry, agricultural aviation can be challenging to get into. We want this infographic to shed some light on that process in a way that will resonate with a younger generation. If you need more information, please visit www.fieldsoarers.example/content/start-here.

Industry/Entity Type

Graphic Designer

Font styles to use
Serif
Sans Serif

Requirements
Must have
• 1) The infographic should follow the general format provided in the Ag-Pilot-Career-Infographic-Concept document. It does not have to literally follow that format (for instance, I used bullet points), but it should convey and, depending on how much creative license you use, at least capture the essence of the factors outlined in the document for becoming an ag pilot. It would be preferable for the infographic to be in portrait format in case it is made into a poster. The infographic should end with our logo and web address.
2) The infographic should also feature illustrations of ag planes (a.k.a. crop dusters), but they have to be of actual agricultural aircraft. An open-cockpit biplane is not an ag plane.
3) All images must be royalty-free and obtained legally. If you choose to use stock art, start with the comp image until the artwork is approved.
Nice to have
• 1) Agricultural images/illustrations, such as corn, wheat or cotton.
2) Icons of a growing crowd of people to illustrate 8.1 billion people by 2025 and a population of 9.6 billion people by 2050.
Should not have
• Crop dusting is an outdated term. Aerial applicators do not apply dust, products are primarily dispensed in liquid form. Therefore, do not use any imagery featuring plumes of smoke coming from the airplane or helicopter. Also, although the current pool of ag pilots is getting older, the infographic should not make them appear geriatric or elderly.

```html
<!DOCTYPE html>
<html lang="en">
<head>
<meta charset="utf-8">
<title>The Hunt for the Nation's Fresh Field Flyers Begins!</title>
<link href="https://fonts.googleapis.com/css2?family=Roboto:wght@300;400;700&family=Oswald:wght@400;500;700&family=Open+Sans:wght@400;600;700&display=swap" rel="stylesheet">
<style>
:root{
  --green-dark:#1f5a0c;
  --green:#3f8f10;
  --green-light:#6cc41a;
  --charcoal:#2a2a2a;
  --charcoal-2:#1c1c1c;
  --orange:#f6a623;
  --blue:#4fb3e8;
  --paper:#eeeeee;
  --ink:#2b2b2b;
  --muted:#6f6f6f;
  --pill:#4a4a4a;
  --red:#d9342b;
  --navy:#16325c;
}
*{margin:0;padding:0;box-sizing:border-box}
html,body{width:867px;height:1200px;overflow:hidden;background:#fff}
.poster{position:relative;width:867px;height:1200px;background:var(--paper);font-family:"Open Sans",Arial,sans-serif;color:var(--ink);overflow:hidden}
.abs{position:absolute}

.hero{left:0;top:0;width:867px;height:208px;background:radial-gradient(ellipse at 60% 40%,var(--green-light) 0%,var(--green) 45%,var(--green-dark) 100%)}
.hero-title{left:68px;top:14px;font-family:"Roboto",sans-serif;font-weight:300;font-size:34px;color:#fff;letter-spacing:.2px;white-space:nowrap}
.hero-art{left:30px;top:66px;width:230px;height:132px;border-radius:6px;background:linear-gradient(160deg,#7fbf3a,#3d6e18)}
.hero-copy{left:290px;top:90px;width:550px;font-size:11.2px;line-height:14px;color:#fff}

.stats{left:0;top:208px;width:867px;height:160px;background:var(--charcoal)}
.stats-chart{left:0;top:208px;width:272px;height:160px;background:var(--charcoal-2)}
.chart-title{left:32px;top:228px;font-family:"Oswald",sans-serif;font-weight:500;font-size:13px;line-height:17px;color:#fff}
.stat-num{font-family:"Oswald",sans-serif;font-weight:500;white-space:nowrap}
.crowd{left:285px;top:222px;width:120px;height:68px;border-radius:3px;background:linear-gradient(#e8e8e8,#bdbdbd);opacity:.85}
.pilots-num{left:290px;top:285px;font-size:44px;color:var(--orange);line-height:50px}
.pilots-label{left:290px;top:340px;font-family:"Oswald",sans-serif;font-size:15px;color:var(--orange);white-space:nowrap}
.age-figure{left:476px;top:218px;width:28px;height:72px;border-radius:3px;background:#e6e6e6}
.age-num{left:514px;top:214px;font-size:64px;line-height:80px;color:var(--blue)}
.age-label{left:466px;top:294px;font-family:"Oswald",sans-serif;font-size:22px;line-height:30px;color:var(--blue);white-space:nowrap}
.acres{left:652px;top:208px;width:215px;height:160px;background:#141414}
.field-art{left:700px;top:222px;width:100px;height:58px;background:linear-gradient(135deg,#8ba354,#5d6a36);transform:skewX(-18deg)}
.acres-num{left:690px;top:280px;font-size:27px;color:#fff}
.acres-label{left:690px;top:318px;font-family:"Oswald",sans-serif;font-size:10.5px;line-height:13px;color:var(--green-light);white-space:nowrap}
.acres-label small{font-size:6px;color:#aaa}

.mouths{left:0;top:368px;width:272px;height:44px;background:var(--charcoal-2);color:#fff;font-family:"Oswald",sans-serif;font-weight:500;font-size:15px;line-height:44px;padding-left:30px;white-space:nowrap}
.right-stuff{left:290px;top:374px;font-family:"Roboto",sans-serif;font-size:16px;line-height:20px;color:#555;white-space:nowrap}
.divider{left:0;top:424px;width:867px;height:9px;background:repeating-linear-gradient(-45deg,#d6d6d6 0 3px,#eeeeee 3px 6px)}

.pill{height:24px;border-radius:12px;background:var(--pill);color:#fff;font-family:"Roboto",sans-serif;font-size:12.5px;line-height:24px;padding:0 16px 0 32px;white-space:nowrap}
.pill .dot{position:absolute;left:-2px;top:-2px;width:28px;height:28px;border-radius:50%}
.pill .glyph{position:absolute;left:5px;top:5px}
.bullets{font-size:8.6px;line-height:11.2px;color:var(--ink);list-style:none}
.bullets li{position:relative}
.bullets li::before{content:"•";position:absolute;left:-22px}
.bullets .sub{font-style:italic;color:#444}
.bullets .sub::before{content:"-"}
.art{border-radius:4px}

.salary-chart{left:70px;top:905px;width:330px;height:195px}
.need-map{left:470px;top:910px;width:370px;height:140px;border-radius:20px;background:radial-gradient(ellipse at 50% 50%,#d6d6d6 0%,#e2e2e2 60%,var(--paper) 100%)}
.people{left:578px;top:928px;width:120px;height:68px;background:linear-gradient(#2aa6c9,#1a7d98);border-radius:3px}
.by-year{left:575px;top:897px;font-family:"Roboto",sans-serif;font-size:13px;color:var(--red);white-space:nowrap}
.by-year b{font-size:24px}
.big96{left:572px;top:994px;font-family:"Roboto",sans-serif;font-size:44px;line-height:44px;color:var(--navy);white-space:nowrap}
.big96 span{font-size:20px;line-height:20px;display:inline-block;vertical-align:top;margin-top:2px;color:#1a7d98}
.to-feed{left:576px;top:1037px;font-family:"Roboto",sans-serif;font-size:12px;color:#1a9bc4;white-space:nowrap}
.conclusion{left:440px;top:1071px;font-size:10.5px;line-height:14px;font-weight:700;color:#111;white-space:nowrap}

.footer-light{left:0;top:1128px;width:360px;height:72px;background:#fff}
.footer-dark{left:330px;top:1128px;width:537px;height:72px;background:#3a3a3a;clip-path:polygon(30px 0,100% 0,100% 100%,0 100%)}
.brand{left:60px;top:1146px;display:flex;align-items:center;gap:10px;font-family:"Roboto",sans-serif;font-weight:700;font-size:20px;color:var(--navy);white-space:nowrap}
.brand i{width:26px;height:26px;border-radius:50%;background:var(--navy);display:block}
.more-info{left:362px;top:1147px;font-family:"Roboto",sans-serif;font-size:20px;color:#e5e5e5;white-space:nowrap}
.more-info b{color:var(--green-light);font-weight:400}
</style>
</head>
<body>
<main class="poster">

  <section class="hero abs"></section>
  <h1 class="hero-title abs">The Hunt for the Nation's Fresh Field Flyers Begins!</h1>
  <div class="hero-art abs" role="img" aria-label="Ag plane flying over a green map of the country"></div>
  <p class="hero-copy abs">Aerial application is an exciting field that combines precision agriculture with low-level aviation to aid farmers in producing a safe, affordable and abundant supply of food, fiber and biofuel. To those who are a part of this unique profession, it's not just a job but a way of life. Becoming an ag pilot isn't easy, but it is worth it. As agriculture's air force ages, the window of opportunity is open for a new generation of ag pilots to step forward and provide the aerial application services the nation's farmers depend on</p>

  <section class="stats abs"></section>
  <div class="stats-chart abs"></div>
  <div class="chart-title abs">BILLION PROJECTED<br>WORLD POPULATION</div>
  <svg class="abs" style="left:28px;top:255px" width="190" height="112" viewBox="0 0 190 112">
    <g font-family="Oswald,sans-serif" font-size="9" fill="#fff" text-anchor="middle">
      <rect x="2" y="55" width="18" height="33" rx="9" fill="#e2573a"/><text x="11" y="72">7.2</text>
      <rect x="28" y="50" width="18" height="38" rx="9" fill="#f6a623"/>
      <rect x="55" y="42" width="18" height="46" rx="9" fill="#a6b83a"/>
      <rect x="82" y="32" width="18" height="56" rx="9" fill="#6fae4a"/><text x="91" y="47">8.1</text>
      <rect x="109" y="20" width="18" height="68" rx="9" fill="#6a9a9a"/>
      <rect x="136" y="8" width="18" height="80" rx="9" fill="#5aa7c2"/>
      <rect x="163" y="-4" width="18" height="92" rx="9" fill="#4fb3e8"/><text x="172" y="12">9.6</text>
      <line x1="11" y1="96" x2="172" y2="96" stroke="#777" stroke-width="1"/>
      <g fill="#f6a623"><circle cx="11" cy="96" r="2.5"/><circle cx="37" cy="96" r="2.5"/><circle cx="64" cy="96" r="2.5"/><circle cx="91" cy="96" r="2.5"/><circle cx="118" cy="96" r="2.5"/><circle cx="145" cy="96" r="2.5"/><circle cx="172" cy="96" r="2.5"/></g>
      <g fill="#bbb" font-size="6.5"><text x="11" y="110">2013</text><text x="91" y="110">2025</text><text x="172" y="110">2050</text></g>
    </g>
  </svg>
  <div class="crowd abs" role="img" aria-label="Rows of small person icons"></div>
  <div class="pilots-num stat-num abs">2.700</div>
  <div class="pilots-label abs">AG PILOT IN U.S</div>
  <div class="age-figure abs" role="img" aria-label="Single person icon"></div>
  <div class="age-num stat-num abs">+50</div>
  <div class="age-label abs">AVERAGE AGE OF<br>AG PILOTS IN U.S</div>
  <div class="acres abs"></div>
  <div class="field-art abs" role="img" aria-label="Square of farm field seen in perspective"></div>
  <div class="acres-num stat-num abs">71 MILLION</div>
  <div class="acres-label abs">ACRES AERIAL APPLICATORS<br>TREAT BY AIR EACH YEAR<br><small>IN THE U.S</small></div>

  <div class="mouths abs">2.4 BILLION MORE MOUTHS TO FEED</div>
  <p class="right-stuff abs">Think you've got the right stuff?<br>Here's what it takes to enter and make it as an ag pilot</p>
  <div class="divider abs"></div>

  <!-- Requirements -->
  <div class="pill abs" style="left:54px;top:451px"><span class="dot" style="background:#3b5fa8"></span><svg class="glyph" width="14" height="14" viewBox="0 0 14 14"><path d="M2 7l3.5 3.5L12 3" fill="none" stroke="#fff" stroke-width="2.4"/></svg>Requirements</div>
  <div class="art abs" style="left:295px;top:440px;width:92px;height:60px;background:linear-gradient(#3a3a3a,#111)" role="img" aria-label="Graduation cap with gold tassel"></div>
  <ul class="bullets abs" style="left:54px;top:488px;width:340px">
    <li>Commercial Pilot Certificate</li>
    <li>Class II Medical Certificate (annual examination)</li>
    <li>Trained and tested in agricultural aircraft operations</li>
    <li class="sub">Ag pilots must pass a knowledge and skills test administered by the Flight Safety Bureau or the pilot's chief operations supervisor.</li>
    <li>State-administered Environmental Board commercial pesticide applicator certification</li>
    <li class="sub">Ag pilots must obtain a pesticide license from each state they fly in demonstrating their knowledge in the handling and application of crop protection products.</li>
    <li>Meet the requirements for insurability in the aircraft and type of flight operations</li>
  </ul>

  <!-- Training options -->
  <div class="pill abs" style="left:432px;top:451px"><span class="dot" style="background:#1e9ad6"></span>Training Options</div>
  <div class="art abs" style="left:678px;top:452px;width:140px;height:30px;background:linear-gradient(90deg,#2f7fa6,#5aa3c6,#2f7fa6)" role="img" aria-label="Pair of pilot wings"></div>
  <ul class="bullets abs" style="left:432px;top:488px;width:410px">
    <li>Preparatory Education</li>
    <li class="sub">Basic flight training program at a flight school, or flight training curriculum at a two- or four-year college</li>
    <li class="sub">Agricultural coursework at a university, college, community college or other institution.<br>(A college degree is not mandatory, but many incoming ag pilots have a degree in agro-science or business. Others have a more aviation-focused education.)</li>
    <li>Attend a flight school specializing in agricultural aviation training</li>
    <li>On the Job Training/Apprentice Program</li>
    <li class="sub">Being trained under an experienced aerial application operator is an excellent way to get the on-the-job training needed to become a safe, efficient ag pilot. This could include learning from the ground up as a mixer/loader for a period of time.</li>
  </ul>

  <!-- Skills -->
  <div class="pill abs" style="left:62px;top:625px"><span class="dot" style="background:var(--red)"></span>Skills / Mindset</div>
  <ul class="bullets abs" style="left:54px;top:660px;width:365px">
    <li>Flying is a big part of the job, but just one of many facets of being an ag pilot.</li>
    <li class="sub">Ag pilots are often referred to as <span style="color:#3f8f10">"farmers in the sky"</span> because of the amount of agricultural knowledge required to ensure the job is completed correctly and safely without incurring economical or environmental damage to persons or property.</li>
    <li class="sub">While being an aircraft mechanic is not a requirement, mechanical knowledge is helpful.</li>
    <li class="sub">Good communication skills to deal with customers and the community are important.</li>
    <li class="sub">Finally, an aspiring ag pilot must have a deep desire to pursue this career path. That fortitude will serve you well</li>
  </ul>

  <!-- Working conditions -->
  <div class="pill abs" style="left:432px;top:625px"><span class="dot" style="background:var(--orange)"></span>Working Conditions</div>
  <div class="art abs" style="left:720px;top:625px;width:92px;height:68px;border-radius:46px 46px 8px 8px;background:linear-gradient(#ffd84a,#e9b300)" role="img" aria-label="Yellow hard hat"></div>
  <ul class="bullets abs" style="left:432px;top:660px;width:285px">
    <li>If you are a <b style="color:#7a5a00">"ROOKIE"</b>, expect one to two years of learning the ground operation with a gradual transition to flight operations.</li>
    <li>During the flying season, expect LONG days.</li>
  </ul>
  <ul class="bullets abs" style="left:432px;top:693px;width:390px">
    <li class="sub">In the summer ag pilots are up and airborne by sunrise. They work until the work runs out, the temperature is too hot to effectively apply product or the sun goes down. In certain areas applications are conducted during nighttime hours as well.</li>
    <li class="sub">During the busy season some operators/pilots work seven days a week while the work is available.</li>
    <li>During the offseason ...</li>
    <li class="sub">Ag pilots complete any required recurring training and earn continuing education credits at state and national agricultural aviation conventions.</li>
    <li class="sub">The seasonal nature of ag flying in many areas may afford ag pilots with the opportunity for time off or to supplement their income through other forms of work.</li>
  </ul>

  <!-- Income -->
  <div class="pill abs" style="left:62px;top:765px"><span class="dot" style="background:#3f8f10"></span><svg class="glyph" width="14" height="14" viewBox="0 0 14 14"><text x="7" y="12" fill="#fff" font-family="Roboto,sans-serif" font-weight="700" font-size="13" text-anchor="middle">$</text></svg>Income Potential</div>
  <div class="art abs" style="left:305px;top:755px;width:62px;height:32px;background:linear-gradient(135deg,#f5d36a,#c99a16)" role="img" aria-label="Stack of banknotes"></div>
  <ul class="bullets abs" style="left:54px;top:800px;width:380px">
    <li>Most ag pilots are paid based on the amount of acres they treat.</li>
    <li class="sub">As a pilot many variables affect the bottom line, such as the type of aircraft you fly, the length of your growing season, type of application and the payment structure from your employer.</li>
    <li>Initially, the pay will be lower while you work on the ground learning the ropes.</li>
    <li>Once you start to fly and perform aerial applications the pay improves.</li>
    <li class="sub">Once in the air many first-year ag pilots can average $20,000~$40,000 depending on the quantity and type of aerial application work performed.</li>
    <li>Skilled aerial applicators can make $60,000~$100,000 a year, the Daily Ledger Review reports.</li>
  </ul>

  <svg class="salary-chart abs" viewBox="0 0 330 195">
    <defs><linearGradient id="area" x1="0" y1="0" x2="0" y2="1"><stop offset="0" stop-color="#f2c98a"/><stop offset="1" stop-color="#f2c98a" stop-opacity=".1"/></linearGradient></defs>
    <path d="M20 105 L45 105 L62 70 L115 70 L135 58 L215 58 L230 40 L262 28 L262 165 L20 165Z" fill="url(#area)"/>
    <path d="M20 105 L45 105 L62 70 L115 70 L135 58 L215 58 L230 40 L262 28" fill="none" stroke="#f6a623" stroke-width="2"/>
    <g fill="#f6a623" opacity=".35"><circle cx="45" cy="105" r="13"/><circle cx="115" cy="70" r="13"/><circle cx="215" cy="58" r="13"/></g>
    <g fill="#fff" stroke="#f6a623" stroke-width="1.5"><circle cx="45" cy="105" r="3"/><circle cx="115" cy="70" r="3"/><circle cx="215" cy="58" r="3"/><circle cx="262" cy="28" r="3"/></g>
    <g stroke="#bbb" stroke-dasharray="2 3"><line x1="45" y1="105" x2="45" y2="165"/><line x1="115" y1="70" x2="115" y2="165"/><line x1="215" y1="58" x2="215" y2="165"/><line x1="262" y1="28" x2="262" y2="165"/></g>
    <line x1="20" y1="10" x2="20" y2="165" stroke="#333" stroke-width="1.5"/>
    <line x1="20" y1="165" x2="300" y2="165" stroke="#333" stroke-width="1.5"/>
    <g fill="#333"><circle cx="30" cy="165" r="3"/><circle cx="80" cy="165" r="3"/><circle cx="130" cy="165" r="3"/><circle cx="180" cy="165" r="3"/><circle cx="230" cy="165" r="3"/><circle cx="280" cy="165" r="3"/></g>
    <text x="60" y="120" font-family="Roboto,sans-serif" font-size="12" fill="#333">$20,000</text>
    <text x="242" y="18" font-family="Roboto,sans-serif" font-size="12" fill="#333">$100,000</text>
    <text x="90" y="183" font-family="Roboto,sans-serif" font-size="11" fill="#333">Skills / Experience</text>
    <text transform="translate(8 105) rotate(-90)" font-family="Roboto,sans-serif" font-size="10" fill="#333">Salary ( $ a year )</text>
  </svg>

  <!-- Need -->
  <div class="pill abs" style="left:446px;top:833px"><span class="dot" style="background:#d43fb0"></span>Need for Aerial Application</div>
  <p class="abs" style="left:440px;top:870px;width:300px;font-size:8.6px;line-height:11.2px">• Aerial application is often the safest, fastest, most efficient and most economical way to treat a crop when pests or disease threaten it.</p>
  <div class="need-map abs" role="img" aria-label="Pale grey world map"></div>
  <div class="by-year abs">By <b>2050</b></div>
  <div class="people abs" role="img" aria-label="Two rows of teal person icons"></div>
  <div class="big96 abs">9.6 <span>Million<br>People</span></div>
  <div class="to-feed abs">To feed on the planet</div>
  <p class="conclusion abs">That's why ...<br>There will always be need for professional, well-trained ag pilots!</p>

  <footer>
    <div class="footer-light abs"></div>
    <div class="footer-dark abs"></div>
    <div class="brand abs"><i></i>Harvest Wing Guild</div>
    <p class="more-info abs">For more information, visit <b>www.fieldsoarers.example</b></p>
  </footer>
</main>
</body>
</html>
```